Stationery and Logo Design Project for new NZ Accounting Firm

Our company name is based in Auckland, New Zealand and is called TMV CA Limited. We are a chartered accountancy firm hence the CA abbreviations.

We need a full logo stationery design: Logo, Letterhead, Business Card and Compliments slip.

We are looking for a bold, modern and clean/simple design that makes us stand out. We want to stand out as professionals in the industry and would like the logo and stationery that our clients see to convey this image. We also want to break away from the traditional boring views of book/bean accountants. We are not doing the same old things others are doing and are mainly cloud based but with face to face business relationship focused as well.

We see ourselves as business advisers that provide more than just filing their tax returns. We want to add value to their business and be a partner in their business ventures.

We want the logo to convey the above and also attract potential clients when they see our ads among the thousands on zarvo and the tallow index.

The logo can be for the "TMV" with CA Ltd seperately or a logo/design beside the TMV. But open to other suggestions or concept.

Hi Designers

The designs I have received so far is not quite what I want.

I want something modern and bold that is DIFFERENT from others, from the usual logo designs. Some logo that when people look at it they will remember it as opposed to fading in the background of other competitors' logo.

Lower case lettering for the TMV could be something to explore as I have not seen a lot of these and they do appeal to me.

Thanks

We can focus on the logo first as that will form the main part for all stationery.

Reason: Final stages of choosing a logo design so need to time for designers to submit the letterhead, namecards designs.

Target Market(s)

Our target clients are small to medium business ranging from the sole trader to 50 employees businesses

Industry/Entity Type

Business

```html
<!DOCTYPE html>
<html lang="en">
<head>
<meta charset="utf-8">
<title>TMV CA Ltd. — Business Card</title>
<link href="https://fonts.googleapis.com/css2?family=Source+Sans+3:ital,wght@0,400;0,600;0,700;1,400&display=swap" rel="stylesheet">
<style>
  :root {
    --navy: #0d1f6b;
    --navy-deep: #06114a;
    --navy-bright: #1a3391;
    --silver: #8a8d94;
    --paper: #ffffff;
    --paper-shade: #e9e9ec;
    --stage: #d9d9dc;
    --ink-light: #f2f4fa;
  }
  * { box-sizing: border-box; margin: 0; padding: 0; }
  html, body { width: 1200px; height: 900px; overflow: hidden; }
  body {
    background: var(--stage);
    font-family: "Source Sans 3", "Myriad Pro", sans-serif;
    position: relative;
  }

  .card { position: absolute; width: 560px; height: 322px; overflow: hidden;
          box-shadow: 0 6px 18px rgba(0,0,0,.18); }

  .wordmark { display: inline-flex; flex-direction: column; align-items: flex-end; font-weight: 700; line-height: 1; }
  .wordmark .name { letter-spacing: 3px; }

  /* back of card */
  .card-back {
    left: 60px; top: 70px;
    background: radial-gradient(ellipse at 55% 40%, var(--navy-bright) 0%, var(--navy) 50%, var(--navy-deep) 100%);
    color: var(--ink-light);
  }
  .card-back .brand { position: absolute; left: 0; right: 0; top: 96px; text-align: center; }
  .card-back .wordmark { color: var(--ink-light); }
  .card-back .wordmark .name { font-size: 64px; }
  .card-back .wordmark .sub { font-size: 22px; margin-top: -2px; }
  .card-back .web {
    position: absolute; left: 0; right: 0; top: 240px; text-align: center;
    font-size: 15px; letter-spacing: 4px; color: var(--ink-light);
  }

  /* front of card */
  .card-front { left: 600px; top: 340px; background: linear-gradient(135deg, var(--paper) 40%, var(--paper-shade)); }
  .card-front svg.wave { position: absolute; inset: 0; }
  .card-front .wordmark { position: absolute; left: 40px; top: 34px; color: var(--navy); }
  .card-front .wordmark .name { font-size: 64px; }
  .card-front .wordmark .sub { font-size: 24px; margin-top: -2px; }

  .holder { position: absolute; left: 24px; top: 250px; width: 250px; text-align: center; color: var(--ink-light); }
  .holder .name { font-size: 19px; font-weight: 700; }
  .holder .role { font-size: 14px; font-style: italic; }
  .divider { position: absolute; left: 286px; top: 222px; width: 1px; height: 72px; background: rgba(255,255,255,.55); }
  .contact { position: absolute; left: 300px; right: 18px; top: 216px; color: var(--ink-light); font-size: 12px; line-height: 1.75; }
  .contact .row { display: flex; gap: 14px; }
  .contact .item { display: flex; align-items: center; gap: 5px; white-space: nowrap; }
  .contact svg { width: 12px; height: 12px; fill: none; stroke: var(--ink-light); stroke-width: 1.6; }

  /* logo panel */
  .logo-panel {
    position: absolute; left: 60px; top: 620px; width: 340px; height: 220px;
    background: var(--paper); display: flex; align-items: center; justify-content: center;
  }
  .logo-panel .wordmark { color: var(--navy); }
  .logo-panel .wordmark .name { font-size: 88px; }
  .logo-panel .wordmark .sub { font-size: 32px; margin-top: -2px; }
</style>
</head>
<body>

  <section class="card card-back">
    <div class="brand">
      <div class="wordmark"><span class="name">TMV</span><span class="sub">CA Ltd.</span></div>
    </div>
    <div class="web">www.tmvca.co.nz</div>
  </section>

  <section class="card card-front">
    <svg class="wave" viewBox="0 0 560 322" width="560" height="322">
      <defs>
        <linearGradient id="band" x1="0" y1="0" x2="1" y2="0">
          <stop offset="0" stop-color="#06114a"/>
          <stop offset=".55" stop-color="#1a3391"/>
          <stop offset="1" stop-color="#0d1f6b"/>
        </linearGradient>
      </defs>
      <path d="M0,200 C150,235 300,215 400,150 C460,110 520,96 560,100 L560,322 L0,322 Z" fill="url(#band)"/>
      <path d="M0,218 C150,252 300,232 402,166 C462,126 522,112 560,116" fill="none" stroke="#ffffff" stroke-width="7"/>
      <path d="M230,222 C320,205 370,150 430,120 C480,96 525,90 560,92" fill="none" stroke="#8a8d94" stroke-width="5"/>
    </svg>
    <div class="wordmark"><span class="name">TMV</span><span class="sub">CA Ltd.</span></div>
    <div class="holder">
      <div class="name">Mara Ellison</div>
      <div class="role">Chartered Accountant</div>
    </div>
    <div class="divider"></div>
    <div class="contact">
      <div class="row"><span class="item">14 Harbour Lane, Northcote, Auckland 0627</span></div>
      <div class="row">
        <span class="item"><svg viewBox="0 0 12 12"><path d="M2,4 Q6,0 10,4 L9,5 L7,4 L5,4 L3,5 Z M3,6 H9 V10 H3 Z"/></svg>(09) 555 0142</span>
        <span class="item"><svg viewBox="0 0 12 12"><circle cx="6" cy="6" r="2"/><path d="M8,6 V7.5 Q10,8 10,6 A4,4 0 1 0 8,9.5"/></svg>info@tmvca.co.nz</span>
      </div>
      <div class="row">
        <span class="item"><svg viewBox="0 0 12 12"><path d="M3,5 V1.5 H9 V5 M2,5 H10 V9 H2 Z M4,8 H8 V11 H4 Z"/></svg>(09) 555 0143</span>
        <span class="item"><svg viewBox="0 0 12 12"><circle cx="6" cy="6" r="4.5"/><path d="M1.5,6 H10.5 M6,1.5 Q3,6 6,10.5 Q9,6 6,1.5"/></svg>www.tmvca.co.nz</span>
      </div>
    </div>
  </section>

  <section class="logo-panel">
    <div class="wordmark"><span class="name">TMV</span><span class="sub">CA Ltd.</span></div>
  </section>

</body>
</html>
```